Torvane Staffing - Mission Poster Design

We are a staffing and recruiting firm with multiple locations across the US. I am seeking a clean modern design highlighting our Mission Statement: Torvane Staffing...Linking Bright Talent with Bold Employers! This design will be framed and placed at the entrance of all of our offices. My website is www.torvanestaffing.example

Target Market(s)

Will be our company mission with a poster prominently placed in each office.

Industry/Entity Type

Staffing

Requirements
Must have
• Must be professional, clean and eye catching. We want to embrace diversity, so we like a variety of people if people will be a focal part.

```html
<!DOCTYPE html>
<html lang="en">
<head>
<meta charset="utf-8">
<title>Torvane Staffing – Mission Poster</title>
<link rel="stylesheet" href="https://fonts.googleapis.com/css2?family=Bebas+Neue&display=swap">
<style>
  :root {
    --paper: #f4f4f4;
    --teal-deep: #00727c;
    --teal-bright: #03a0ae;
    --teal-pale: #8cc8d0;
    --navy: #2a2560;
    --white: #ffffff;
    --shadow: rgba(0, 40, 45, 0.55);
  }
  * { margin: 0; padding: 0; box-sizing: border-box; }
  html, body { width: 910px; height: 1200px; overflow: hidden; background: var(--paper); }
  .poster {
    position: relative;
    width: 910px;
    height: 1200px;
    overflow: hidden;
    font-family: "Bebas Neue", "Arial Narrow", sans-serif;
    color: var(--white);
  }
  .poster-background { position: absolute; inset: 0; }
  .brand-name {
    position: absolute;
    top: 125px;
    left: 0;
    width: 100%;
    text-align: center;
    font-size: 104px;
    font-weight: 400;
    line-height: 1;
    letter-spacing: 2px;
    color: var(--navy);
  }
  .quote-mark {
    position: absolute;
    top: 418px;
    left: 0;
    width: 100%;
    text-align: center;
    font-family: Georgia, "Times New Roman", serif;
    font-weight: 700;
    font-size: 210px;
    line-height: 1;
    height: 110px;
    overflow: hidden;
    text-shadow: 0 2px 8px var(--shadow);
  }
  .mission-statement {
    position: absolute;
    top: 568px;
    left: 0;
    width: 100%;
    text-align: center;
    font-size: 134px;
    line-height: 127px;
    letter-spacing: 1px;
    text-shadow: 0 3px 10px var(--shadow);
  }
  .mission-statement span { display: block; }
  .website {
    position: absolute;
    top: 1115px;
    left: 0;
    width: 100%;
    text-align: center;
    font-size: 30px;
    line-height: 1;
    letter-spacing: 0.5px;
    white-space: nowrap;
    text-shadow: 0 2px 6px var(--shadow);
  }
</style>
</head>
<body>
<main class="poster">
  <svg class="poster-background" width="910" height="1200" viewBox="0 0 910 1200" aria-hidden="true">
    <defs>
      <linearGradient id="pale-band" x1="0" y1="0" x2="1" y2="0">
        <stop offset="0.2" stop-color="#ffffff" stop-opacity="0"/>
        <stop offset="0.65" stop-color="#8cc8d0"/>
        <stop offset="1" stop-color="#14aab6"/>
      </linearGradient>
      <linearGradient id="bright-band" x1="0" y1="0" x2="1" y2="0">
        <stop offset="0" stop-color="#00727c"/>
        <stop offset="1" stop-color="#03a0ae"/>
      </linearGradient>
      <linearGradient id="office-photo-tone" x1="0" y1="0" x2="0" y2="1">
        <stop offset="0" stop-color="#00727c" stop-opacity="0"/>
        <stop offset="0.5" stop-color="#0a6a72"/>
        <stop offset="1" stop-color="#055a62"/>
      </linearGradient>
    </defs>
    <rect class="paper" width="910" height="1200" fill="var(--paper)"/>
    <polygon class="pale-band" points="0,300 910,369 910,417 0,324" fill="url(#pale-band)"/>
    <polygon class="teal-field" points="0,324 910,463 910,1200 0,1200" fill="var(--teal-deep)"/>
    <polygon class="bright-band" points="0,324 910,417 910,463" fill="url(#bright-band)"/>
    <rect class="office-photo" x="0" y="680" width="910" height="520" fill="url(#office-photo-tone)"
          role="img" aria-label="Faded teal-toned photo of a busy open-plan office with people working at desks"/>
    <g class="quote-frame" fill="none" stroke="var(--white)" stroke-width="4">
      <polyline points="393,496 113,496 113,1131 262,1131"/>
      <polyline points="517,496 798,496 798,1131 648,1131"/>
    </g>
  </svg>

  <h1 class="brand-name">Torvane Staffing</h1>

  <div class="quote-mark" aria-hidden="true">&ldquo;</div>

  <p class="mission-statement">
    <span>Linking</span>
    <span>Bright Talent</span>
    <span>with Bold</span>
    <span>Employers!</span>
  </p>

  <p class="website">www.torvanestaffing.example</p>
</main>
</body>
</html>
```